Need a new updated business logo and business cards and possible car signs. Logo should be modern with bold elements. Possible use in some way of former logo may be considered. Looking for use of bold colors to grab attention with car signage/wrap in mind. Phone number should be easy to read- customers should understand what business is about- home painting, repair, renovation, 're-imagine your space' etc.

Target Market(s)

Homeowners, construction, businesses

Industry/Entity Type

Contractor

Contact Information for Business Card

Brennick Painting & Renovation, Inc.
Owner : Marcus D. Brennick
919-555-0173
marcusdbrennickmb@larkpost.com
All work is guaranteed and insured! More than 30 years of experience:
residential & commercial, Interior & Exterior, Renovation/Restoration

Logo Text

Brennick Painting & Renovation, Inc. 'Hard Working & Trustworthy'

Other font styles liked:
• Designer suggestions for industry

Colors

Designer to choose colors to be used in the design.

Requirements
Must have
• New design logo-possibly incorporating old elements- new logo ok without old though as well. Cell Phone number has to be on there- Color preferable
Nice to have
• Nice to have a logo that pops and that may be used in conjunction with his parent company Brennick HOLM Estates, LLC.
• Business card layout of information that is clear & easy to read
Should not have
• Bulky old fonts

```html
<!DOCTYPE html>
<html lang="en">
<head>
<meta charset="utf-8">
<title>Brennick Painting &amp; Renovation, Inc. — Business Cards</title>
<link href="https://fonts.googleapis.com/css2?family=Lato:wght@400;700;900&display=swap" rel="stylesheet">
<style>
  :root{
    --canvas:#ece8e3;
    --charcoal:#3a3a3c;
    --charcoal-deep:#2f2f31;
    --brand-red:#a5161d;
    --paper:#ffffff;
    --ink:#2b2b2b;
    --rule:#8a8a8c;
    --muted:#e4e4e4;
  }
  *{box-sizing:border-box;margin:0;padding:0}
  html,body{width:1200px;height:900px;overflow:hidden}
  body{background:var(--canvas);font-family:"Lato",sans-serif;position:relative}

  .card{position:absolute;width:570px;height:326px;border-radius:3px;overflow:hidden;
        box-shadow:0 14px 30px rgba(0,0,0,.22),0 2px 6px rgba(0,0,0,.15)}

  /* Back card */
  .card--back{left:70px;top:120px;background:var(--charcoal);color:var(--muted);text-align:center}
  .card--back .wordmark{margin-top:70px}
  .wordmark__name{display:block;color:var(--brand-red);font-weight:900;letter-spacing:1px;line-height:1}
  .wordmark__sub{display:block;color:var(--brand-red);font-weight:900;letter-spacing:.5px;margin-top:6px}
  .card--back .wordmark__name{font-size:50px}
  .card--back .wordmark__sub{font-size:13px}
  .card--back .divider{width:300px;height:1px;background:var(--rule);margin:24px auto 20px}
  .card--back .services{font-size:15px;line-height:1.55;color:#e9e9e9}

  /* Front card */
  .card--front{left:560px;top:440px;background:var(--paper)}
  .card--front .wordmark{position:absolute;right:34px;top:30px;text-align:right}
  .card--front .wordmark__name{font-size:38px}
  .card--front .wordmark__sub{font-size:11px}
  .contact{position:absolute;left:32px;top:118px;color:var(--ink)}
  .contact__title{color:var(--brand-red);font-size:18px;margin-bottom:8px}
  .contact__row{display:flex;align-items:flex-start;gap:9px;font-size:16px;line-height:1.3;margin-bottom:3px}
  .contact__row svg{flex:none;margin-top:3px}
  .contact__row--phone{font-size:19px}
  .wave{position:absolute;left:0;top:0}
  .guarantee{position:absolute;right:22px;bottom:40px;color:#fff;font-weight:900;font-size:12px;letter-spacing:.3px;transform:rotate(-9deg);transform-origin:right bottom}
</style>
</head>
<body>

<section class="card card--back" aria-label="Business card back">
  <div class="wordmark">
    <span class="wordmark__name">BRENNICK</span>
    <span class="wordmark__sub">PAINTING &amp; RENOVATION, Inc.</span>
  </div>
  <div class="divider"></div>
  <p class="services">More than 30 years of experience.<br>
  Residential &amp; Commercial &nbsp;|&nbsp; Interior &amp; Exterior<br>
  Renovation/Restoration</p>
</section>

<section class="card card--front" aria-label="Business card front">
  <svg class="wave" width="570" height="326" viewBox="0 0 570 326" aria-hidden="true">
    <path d="M0,262 C150,256 300,222 430,150 C330,232 160,282 0,292 Z" fill="var(--brand-red)"/>
    <path d="M0,300 C170,296 330,250 450,185 C500,160 540,148 570,146 L570,326 L0,326 Z" fill="var(--charcoal)"/>
  </svg>

  <div class="wordmark">
    <span class="wordmark__name">BRENNICK</span>
    <span class="wordmark__sub">PAINTING &amp; RENOVATION, Inc.</span>
  </div>

  <div class="contact">
    <p class="contact__title">Contact Our Team:</p>
    <p class="contact__row contact__row--phone">
      <svg width="12" height="17" viewBox="0 0 12 17" aria-hidden="true"><rect x="1" y="1" width="10" height="15" rx="2" fill="none" stroke="var(--brand-red)" stroke-width="1.8"/><circle cx="6" cy="13" r="1" fill="var(--brand-red)"/></svg>
      919-555-0173
    </p>
    <p class="contact__row">
      <svg width="14" height="11" viewBox="0 0 14 11" aria-hidden="true"><rect width="14" height="11" rx="1" fill="var(--brand-red)"/><path d="M1,1 L7,6 L13,1" fill="none" stroke="#fff" stroke-width="1.3"/></svg>
      marcusdbrennickmb@larkpost.com
    </p>
    <p class="contact__row">
      <svg width="13" height="18" viewBox="0 0 13 18" aria-hidden="true"><path d="M6.5,0 C10.1,0 13,2.8 13,6.4 C13,11 6.5,18 6.5,18 C6.5,18 0,11 0,6.4 C0,2.8 2.9,0 6.5,0 Z" fill="var(--brand-red)"/><circle cx="6.5" cy="6.4" r="2.4" fill="#fff"/></svg>
      <span>58 Alder Ridge Court<br>Oakvale, NC 27099</span>
    </p>
  </div>

  <p class="guarantee">ALL WORK IS GUARANTEED AND INSURED!</p>
</section>

</body>
</html>
```